Qortvax@mailvane.net

I am making this a landing page and I want to really grab the person and get them to call. So, I want some up front language at the top language about why they should contact me right away. The person looking is in a tough spot, they woe a lot of debt, they do not want to file a bankruptcy for moral or personal reasons, I want them to know that bankruptcy is a legal process that can help them and that they should not fear checking out their options. I will give them all of the information and if they want to go further fine, if not, they will have a lot more information about their situation and options

The language at the top, I want to be

Thanks for visiting us. You came here because you are having debt problems and you want solutions. Yes, we want your business. But, we don't want it if it is not right for you. We have been at this a long time and assisted thousands of Hawaii people and families with their debt problems. Many of those people were referred by former clients, but, our biggest referral source is people who did not file a bankruptcy. The reason is simple- our absolutely free and confidential consultation will help you get a handle on your whole situation. We will discuss your assets, your debts, your income and expenses and get a complete picture. It is only with this complete global picture of your particular situation that you can know your options, all of them, and then you can decide what is right for you. You are the driver. Call us at 472-3000 (from all islands) and let us help you today!

The color should be calming without being wimpy.

i want the top to be simple and a call to action giving people the sense that we know what we are doing and that they can call us for truly no obligation and we can help them diagnose their money issues and I can give them their options and they can do whatever they wish with them.

Hawaii people between ages of 28-70 who have credit card, loan or mortgage problems and need a way to get out of their debt

Legal

• Must incorporate the items at plkwindra.com. May be helpful to look at owezerozumbo.com for example of the "clean clear" landing I would like to "grab" the customer's attention and get them to call me, phone is better than email. So must have contact us too.

```html
<!DOCTYPE html>
<html lang="en">
<head>
<meta charset="utf-8">
<title>Keoni R. Halversen, Attorney-at-Law</title>
<link href="https://fonts.googleapis.com/css2?family=Open+Sans:ital,wght@0,400;0,600;1,400&family=PT+Sans&display=swap" rel="stylesheet">
<style>
:root{
  --header-dark:#4a1a08;
  --header-mid:#7a3414;
  --nav-dark:#3c2a22;
  --nav-mid:#5a463c;
  --tab:#efe0c8;
  --brown:#6e4634;
  --brown-text:#5b2e1a;
  --peach-1:#fdebd2;
  --peach-2:#f7d9b2;
  --cream:#f6eee6;
  --line:#d9cdc3;
  --body-text:#4a4a4a;
  --heading:#2d2d2d;
  --brand-text:#f3e6d2;
  --white:#ffffff;
}
*{margin:0;padding:0;box-sizing:border-box}
html,body{width:791px;height:1200px;overflow:hidden}
body{position:relative;background:var(--white);font-family:"Open Sans",Arial,sans-serif;color:var(--body-text)}
.abs{position:absolute}

/* header */
.site-header{left:0;top:0;width:791px;height:135px;background:linear-gradient(180deg,var(--header-dark) 0,var(--header-mid) 55%,#6a2c10 100%)}
.brand{left:24px;top:40px;width:170px;font-family:"Open Sans",sans-serif;font-weight:600;font-size:17px;line-height:1.3;color:var(--brand-text)}
.call-ribbon{left:594px;top:12px;width:160px;height:76px}
.call-ribbon .label{position:absolute;left:18px;top:11px;font-size:12px;color:#5a3a26;letter-spacing:.3px}
.call-ribbon .phone{position:absolute;left:20px;top:28px;font-size:19px;color:var(--brown-text)}

/* nav */
.main-nav{left:0;top:135px;width:791px;height:43px;background:linear-gradient(180deg,var(--nav-mid),var(--nav-dark))}
.main-nav ul{list-style:none;display:flex;height:100%}
.main-nav li{font-family:"PT Sans",sans-serif;font-size:13px;color:#f3ebe4;display:flex;align-items:center;justify-content:center;border-right:1px solid #6f5d53;height:100%}
.main-nav li.active{background:var(--tab);color:var(--brown-text);border-right:none}

/* hero */
.hero-photo{left:27px;top:186px;width:504px;height:226px;background:linear-gradient(160deg,#6a4428 0,#8b5a34 40%,#3b2a24 100%);border:3px solid #e5d4bb}
.hero-caption{left:30px;top:377px;width:498px;height:31px;background:rgba(230,230,230,.72);font-size:13px;color:#222;padding:6px 0 0 15px}
.hero-panel{left:534px;top:186px;width:232px;height:227px;background:linear-gradient(180deg,var(--peach-1),var(--peach-2));border:1px solid #e4c7a0;padding:17px 14px 0 15px;box-shadow:0 4px 6px rgba(0,0,0,.12)}
.hero-panel h2{font-weight:400;font-size:15.5px;color:#3c3c3c;line-height:1.45}
.hero-panel h2 b{font-weight:600}
.hero-panel p{font-size:8px;line-height:1.42;color:#7a6555;margin-top:5px}
.btn{display:inline-block;background:var(--brown);color:#f4ece6;font-size:8.5px;border-radius:3px;letter-spacing:.2px}
.hero-panel .btn{margin-top:9px;padding:4px 0;width:101px;text-align:center}

/* about */
.about{left:34px;top:443px;width:500px}
.section-title{font-size:14.5px;font-weight:400;color:var(--heading)}
.about .section-title{border-bottom:1px solid #cfcfcf;padding-bottom:4px;width:440px}
.about p{font-size:8px;line-height:1.4;margin-top:7px}
.about p + p{margin-top:3px}

.link-box{top:563px;width:156px;height:180px;border:1px solid var(--line);background:var(--white);box-shadow:0 3px 4px rgba(0,0,0,.08)}
.link-box h3{background:var(--brown);color:var(--white);font-weight:400;font-size:12.5px;padding:2px 12px;height:21px}
.link-box ul{list-style:none;padding:12px 8px 0 12px}
.link-box li{font-size:8px;line-height:1.25;color:#4a2a1c;margin-bottom:7px;padding-left:10px;position:relative}
.link-box li::before{content:"";position:absolute;left:0;top:3px;border-left:4px solid #777;border-top:2.5px solid transparent;border-bottom:2.5px solid transparent}

.videos{left:26px;top:759px;width:500px}
.video-thumb{left:26px;top:785px;width:153px;height:132px;background:linear-gradient(180deg,#8a6a4e,#4b3a30)}
.video-bar{left:26px;top:902px;width:153px;height:15px;background:#1d1d1d}
.video-text{left:193px;top:784px;width:330px;font-size:8.1px;line-height:1.45}
.video-text p + p{margin-top:4px}

/* sidebar */
.categories{left:565px;top:441px;width:210px}
.categories ul{list-style:none;margin-top:8px;padding:2px 0 4px 15px;background:linear-gradient(90deg,var(--white) 40%,#ecebeb 100%);height:172px}
.categories li{font-size:8.5px;color:#3a3a3a;line-height:16.6px;padding-left:10px;position:relative}
.categories li::before{content:"";position:absolute;left:0;top:5px;width:4px;height:4px;border-right:1px solid #555;border-top:1px solid #555;transform:rotate(45deg)}
.testimonials{left:560px;top:662px;width:215px}
.quote{left:560px;width:214px;height:78px;background:#f0eded;border:1px solid #e0dada;font-style:italic;font-size:8.1px;line-height:1.65;color:#3a3a3a;padding:7px 8px 0 9px;letter-spacing:-.1px}
.testimonials-btn{left:562px;top:852px;width:122px;height:20px;padding-top:4px;text-align:center;border-radius:4px}

/* footer */
.site-footer{left:0;top:942px;width:791px;height:258px;background:var(--cream);border-top:1px solid #e6d8cc}
.footer-col h4{font-weight:400;font-size:9.5px;color:#222;letter-spacing:.2px}
.divider{top:964px;width:1px;height:110px;background:#d7c9bd}
.quick-links{left:20px;top:960px}
.quick-links .grid{display:grid;grid-template-columns:70px 70px;row-gap:9px;margin-top:15px;font-size:7.8px;line-height:11px;color:#333}
.connect{left:202px;top:960px}
.social{display:flex;gap:4px;margin-top:14px}
.social span{width:21px;height:21px;background:#7a95b8;border-radius:2px}
.social-names{font-size:8px;margin-top:10px;color:#333}
.contact-form{left:395px;top:958px}
.field{width:157px;height:15px;background:var(--white);border:1px solid #d4c9bf;font-size:7.5px;color:#8a8a8a;padding:2px 6px;margin-top:5px}
.field.message{height:64px}
.send{left:395px;top:1111px;width:46px;height:14px;font-size:7.5px;text-align:center;padding-top:2px;border-radius:3px}
.contact-info{left:602px;top:960px;font-size:8.2px;line-height:1.95;color:#333}
.contact-info strong{font-weight:600}
.contact-info .mail{text-decoration:underline}
.copyright{left:11px;top:1153px;width:751px;height:31px;border:1px solid #dcc9b8;border-radius:6px;background:#f1e6dc;font-size:8.8px;color:#555;display:flex;justify-content:space-between;align-items:center;padding:0 16px}
</style>
</head>
<body>

<header class="site-header abs">
  <div class="brand abs">Keoni R. Halversen<br>Attorney-at-Law</div>
  <div class="call-ribbon abs">
    <svg width="160" height="76" viewBox="0 0 160 76" aria-hidden="true">
      <defs><linearGradient id="ribbonFill" x1="0" y1="0" x2="0" y2="1"><stop offset="0" stop-color="#fbefd9"/><stop offset="1" stop-color="#e8d2ad"/></linearGradient></defs>
      <path d="M0 0H160V60L80 76L0 60Z" fill="url(#ribbonFill)"/>
    </svg>
    <span class="label">CALL US NOW:</span>
    <span class="phone">808-472-3000</span>
  </div>
</header>

<nav class="main-nav abs">
  <ul>
    <li class="active" style="width:74px;margin-left:23px">HOME</li>
    <li style="width:127px">ABOUT US</li>
    <li style="width:118px">CHAPTER 7</li>
    <li style="width:107px">CHAPTER 13</li>
    <li style="width:117px">BLOG</li>
    <li style="width:120px;border-right:none">CONTACT US</li>
  </ul>
</nav>

<div class="hero-photo abs" role="img" aria-label="Portrait of the attorney in a dark suit standing before shelves of law books"></div>
<div class="hero-caption abs">You are the driver. We help you see every option.</div>
<section class="hero-panel abs">
  <h2>HAVING <b>DEBT PROBLEMS?</b><br>LET'S TALK, FREE</h2>
  <p>Thanks for visiting us. You came here because you are having debt problems and you want solutions. Yes, we want your business. But, we don't want it if it is not right for you.</p>
  <p>We have been at this a long time and assisted thousands of Hawaii people and families with their debt problems.</p>
  <span class="btn">CALL 808-472-3000</span>
</section>

<section class="about abs">
  <h2 class="section-title">A little About Our Firm</h2>
  <p>Many of those people were referred by former clients, but, our biggest referral source is people who did not file a bankruptcy. The reason is simple- our absolutely free and confidential consultation will help you get a handle on your whole situation. We will discuss your assets, your debts, your income and expenses and get a complete picture.</p>
  <p>It is only with this complete global picture of your particular situation that you can know your options, all of them, and then you can decide what is right for you. You are the driver. Call us at 472-3000 (from all islands) and let us help you today!</p>
</section>

<section class="link-box abs" style="left:26px">
  <h3>Recent &nbsp;Articles</h3>
  <ul>
    <li>What Is Lien Stripping in a Chapter 13 Hawaii Bankruptcy?</li>
    <li>What Is A Co-Debtor Stay in a Chapter 13 Hawaii Bankruptcy?</li>
    <li>What is Chapter 13 Bankruptcy in Hawaii?</li>
    <li>What is Chapter 7 Bankruptcy in Hawaii?</li>
    <li>What is a Hawaii bankruptcy estate?</li>
  </ul>
</section>
<section class="link-box abs" style="left:186px">
  <h3>Recent Videos</h3>
  <ul>
    <li>What Is Lien Stripping in a Chapter 13 Hawaii Bankruptcy?</li>
    <li>What Is A Co-Debtor Stay in a Chapter 13 Hawaii Bankruptcy?</li>
    <li>What is Chapter 13 Bankruptcy in Hawaii?</li>
    <li>What is Chapter 7 Bankruptcy in Hawaii?</li>
    <li>What is a Hawaii bankruptcy estate?</li>
  </ul>
</section>
<section class="link-box abs" style="left:345px">
  <h3>Resources</h3>
  <ul>
    <li>What Is Lien Stripping in a Chapter 13 Hawaii Bankruptcy?</li>
    <li>What Is A Co-Debtor Stay in a Chapter 13 Hawaii Bankruptcy?</li>
    <li>What is Chapter 13 Bankruptcy in Hawaii?</li>
    <li>What is Chapter 7 Bankruptcy in Hawaii?</li>
    <li>What is a Hawaii bankruptcy estate?</li>
  </ul>
</section>

<h2 class="section-title videos abs">Latest Vedios</h2>
<div class="video-thumb abs" role="img" aria-label="Video still of the attorney speaking at his desk"></div>
<div class="video-bar abs">
  <svg width="153" height="15" viewBox="0 0 153 15" aria-hidden="true">
    <path d="M9 4L14 7.5L9 11Z" fill="#ccc"/>
    <rect x="0" y="0" width="153" height="2" fill="#c0392b"/>
  </svg>
</div>
<div class="video-text abs">
  <p>Lanivo Webworks provides you the Search Engine Optimization making your website search engine friendly. So that the website can achieve top position and ranking in the Internet searches and thereby increasing the scope for the website to be found by customers. We here modify the site to improve the ranking by using the keywords and contents.</p>
  <p>E-Commerce is a major progress in technology that has changed the way in which the customers now purchase information, products and the services. It's the new way of providing an opportunity to make your products and services available in the global market 24 hours a day through Internet</p>
</div>

<aside class="categories abs">
  <h2 class="section-title">Our Categories</h2>
  <ul>
    <li>Articles</li><li>bankruptcy</li><li>Bankruptcy Hawaii</li><li>Bankruptcy Honolulu</li><li>bankruptcy oahu</li><li>Blog</li><li>Blogroll</li><li>CARE</li><li>chapter 13</li><li>Chapter 13 Bankruptcy Hawaii</li>
  </ul>
</aside>
<h2 class="section-title testimonials abs">Testimonials</h2>
<blockquote class="quote abs" style="top:684px">"Thanks for the good news about R's plan.... I also want to say thank you for always treating my mother with consideration. Your mindfulness, acuity, and helpfulness will always be remembered..."--HT</blockquote>
<blockquote class="quote abs" style="top:768px">"Thanks for the good news about R's plan.... I also want to say thank you for always treating my mother with consideration. Your mindfulness, acuity, and helpfulness will always be remembered..."--HT</blockquote>
<span class="btn testimonials-btn abs">VIEW MORE TESTIMONAILS</span>

<footer class="site-footer abs"></footer>
<div class="divider abs" style="left:173px"></div>
<div class="divider abs" style="left:376px"></div>
<div class="divider abs" style="left:577px"></div>

<section class="footer-col quick-links abs">
  <h4>QUICK LINKS</h4>
  <div class="grid">
    <span>MAIN PAGE</span><span>BLOG</span>
    <span>ABOUT US</span><span>TESTIMONIALS</span>
    <span>CHAPTER 7</span><span>CONTACT US</span>
    <span>CHAPTER 13</span><span></span>
  </div>
</section>
<section class="footer-col connect abs">
  <h4>LET'S CONNECT WITH US</h4>
  <div class="social"><span></span><span></span><span></span><span></span></div>
  <p class="social-names">Kivora &nbsp;|&nbsp; Chirplo &nbsp;|&nbsp; Netlinka &nbsp;|&nbsp; Frendara</p>
</section>
<section class="footer-col contact-form abs">
  <h4>CONTAC FORM</h4>
  <div class="field" style="margin-top:10px">your name</div>
  <div class="field">your email add</div>
  <div class="field">your phone no.</div>
  <div class="field message">message here</div>
</section>
<span class="btn send abs">SEND</span>
<section class="footer-col contact-info abs">
  <h4>CONTACT INFORMATION</h4>
  <div style="margin-top:4px;padding-left:3px">
    <strong>Keoni R. Halversen,</strong><br>
    Attorney-at-Law<br>
    2240 Kapena St. Suite 410<br>
    Honolulu, HI 96813<br>
    808-472-3000<br>
    <span class="mail">info@plkwindra.com</span>
  </div>
</section>

<div class="copyright abs">
  <span>Copyright © 2012 Company Name &nbsp;|&nbsp; All right reserved</span>
  <span>Privacy Policy &nbsp;|&nbsp; Terms &amp; Conditions</span>
</div>

</body>
</html>
```